out of the box Business Card Design for a Manufacturer / Distributor

We are a manufarturer and distributor of products.
the company name is VORTANI (Pic attached)

the picture is NOT a must have on the business Card.

the Business Card should look really professional and/or special, so out of the box thinking is welcome.

there should be 2 Adresses on the Business Card for Main and Branch Office.
Email Adress, homepage, Name is required
NO Phone Number

Our working field:
Private Labeling
high Quality Production
direct distribution
warehousing
trademark registration
legal support

Main Office:
Kornblumenweg 14
08352 Burgstädt
Germany

Branch Office:
Daska Lane
Sialkot
Pakistan

Names:
Lukas Feldhaus (Owner)
Imran Qureshi (Owner)

Email:
lukas@vortani-example.com
imran@vortani-example.com

homepage:
vortani-example.com

Industry/Entity Type

Manufacturer Distributer

Contact Information for Business Card

Vortani

Requirements
Must have
• Names, both office Adresses, email, homepage
Should not have
• Phone Number

```html
<!DOCTYPE html>
<html lang="en">
<head>
<meta charset="utf-8">
<title>Vortani Business Card</title>
<link href="https://fonts.googleapis.com/css2?family=Montserrat:wght@400;500;700&family=Arimo:wght@400;700&display=swap" rel="stylesheet">
<style>
  :root {
    --canvas: #e8e9eb;
    --card: #444444;
    --ink: #ffffff;
    --rule: #d9d9d9;
    --mark-dark: #1c1c1c;
  }
  * { margin: 0; padding: 0; box-sizing: border-box; }
  html, body { width: 1051px; height: 1200px; overflow: hidden; }
  body {
    background: var(--canvas);
    font-family: "Montserrat", sans-serif;
    color: var(--ink);
    position: relative;
  }
  .card {
    position: absolute;
    left: 83px;
    width: 894px;
    height: 510px;
    background: var(--card);
    box-shadow: 0 6px 22px rgba(0,0,0,.28);
    overflow: hidden;
  }
  .card--front { top: 69px; }
  .card--back { top: 611px; }

  .brand {
    position: absolute;
    display: flex;
    align-items: center;
    gap: 16px;
    font-family: "Montserrat", sans-serif;
    font-weight: 500;
    line-height: 1;
    white-space: nowrap;
  }
  .brand__dot { border-radius: 50%; flex: none; }
  .brand--front { right: 42px; top: 62px; font-size: 66px; color: var(--ink); }
  .brand--front .brand__dot { width: 44px; height: 44px; background: var(--ink); }
  .brand--back { left: 50%; top: 147px; transform: translateX(-50%); font-size: 96px; color: var(--mark-dark); gap: 22px; }
  .brand--back .brand__dot { width: 64px; height: 64px; background: var(--mark-dark); }

  .owners {
    position: absolute; left: 45px; top: 262px;
    font-weight: 700; font-size: 36px; line-height: 44px; white-space: nowrap;
  }
  .owners__role { font-weight: 400; font-size: 22px; margin-left: 2px; }
  .rule {
    position: absolute; left: 45px; top: 324px; width: 807px; height: 2px; background: var(--rule);
  }
  .contacts { position: absolute; left: 45px; top: 335px; list-style: none; }
  .contacts li {
    display: flex; align-items: center; gap: 14px;
    font-size: 24px; height: 40px; white-space: nowrap;
  }
  .contacts svg { width: 22px; height: 22px; flex: none; }
  .branch {
    position: absolute; right: 42px; top: 332px; text-align: right;
    font-size: 24px; line-height: 35px; font-style: normal;
  }
  .branch strong, .main-office strong { font-weight: 700; }
  .main-office {
    position: absolute; left: 0; right: 0; top: 458px; text-align: center;
    font-size: 24px; line-height: 34px; font-style: normal; padding-right: 16px;
  }

  .fields {
    position: absolute; left: 0; right: 0; top: 331px; text-align: center;
    font-family: "Arimo", sans-serif; font-size: 24px;
  }
  .fields__title { font-weight: 700; line-height: 30px; margin-bottom: 13px; }
  .fields__list { list-style: none; line-height: 43px; }
  .fields__list li { display: inline; }
  .fields__list li::before { content: "\2022\00a0"; }
  .fields__list li + li { margin-left: 10px; }
</style>
</head>
<body>
  <section class="card card--front">
    <div class="brand brand--front"><span class="brand__dot"></span>VORTANI</div>
    <h1 class="owners">Lukas Feldhaus | Imran Qureshi <span class="owners__role">(Owner)</span></h1>
    <div class="rule"></div>
    <ul class="contacts">
      <li><svg viewBox="0 0 22 22"><rect x="1" y="5" width="20" height="13" fill="none" stroke="#fff" stroke-width="1.6"/><path d="M1 5l10 8 10-8M1 18l7-7M21 18l-7-7" fill="none" stroke="#fff" stroke-width="1.6"/></svg>lukas@vortani-example.com</li>
      <li><svg viewBox="0 0 22 22"><rect x="1" y="5" width="20" height="13" fill="none" stroke="#fff" stroke-width="1.6"/><path d="M1 5l10 8 10-8M1 18l7-7M21 18l-7-7" fill="none" stroke="#fff" stroke-width="1.6"/></svg>imran@vortani-example.com</li>
      <li><svg viewBox="0 0 22 22"><circle cx="11" cy="11" r="9.5" fill="none" stroke="#fff" stroke-width="1.6"/><path d="M2 11h18M11 1.5c-3.5 3-3.5 16 0 19M11 1.5c3.5 3 3.5 16 0 19" fill="none" stroke="#fff" stroke-width="1.4"/></svg>vortani-example.com</li>
    </ul>
    <address class="branch"><strong>Branch Office:</strong><br>Daska Lane Sialkot<br>Pakistan</address>
    <address class="main-office"><strong>Main Office:</strong> Kornblumenweg 14 08352 Burgstädt Germany</address>
  </section>

  <section class="card card--back">
    <div class="brand brand--back"><span class="brand__dot"></span>VORTANI</div>
    <div class="fields">
      <p class="fields__title">Our working field:</p>
      <ul class="fields__list">
        <li>Private Labeling</li>
        <li>high Quality Production</li>
        <li>direct distribution</li><br>
        <li>warehousing</li>
        <li>trademark registration</li>
        <li>legal support</li>
      </ul>
    </div>
  </section>
</body>
</html>
```